Organic Vegan Crispread - 100% Free of Soja

We are looking to update our labels for our current range of Crispbreads. They are all produced in Denmark, they are organic, vegan og we do not use any soy at all.

The crisp breads are high products and aimed for the gourmet market retail.

The range contains 6 different at the moment and will have 4 new types coming soon. The current six products are following:
Organic Crispbread Salt
Organic Crispbread Herbs
Organic Crispbread spices
Organic Crispbread Seaweed
Organic Crispbread Glutenfree
Organic Cripsbread Protein (Green Proteins)

The range will have to contain our logo and our name.

Measurements of Labels:
60mm wide
50mm High

Only front label design.

Target Market(s)

High End Consumers

Requirements
Must have
• Company Logo
Organic logo red (under this we need to write "QX-VAL-738")
Organic logo Green (under this we need to write "EU / ikke EU-jordbrug")
Name
Visuel identity per type
Nice to have
• Red line throughout the range
Should not have
• No Bling Bling

```html
<!DOCTYPE html>
<html lang="en">
<head>
<meta charset="utf-8">
<title>Organic Crispbread – Label Range</title>
<link href="https://fonts.googleapis.com/css2?family=Amatic+SC:wght@700&family=Oswald:wght@500&family=Open+Sans:wght@400&display=swap" rel="stylesheet">
<style>
  :root {
    --page: #eef0f0;
    --card: #ffffff;
    --ink: #111111;
    --text: #222222;
    --claim-green: #8cc63f;
    --eu-green: #8cc63f;
    --cert-red: #e2231a;
    --herbs: #a3a537;
    --salt: #95c83d;
    --spices: #f48120;
    --seaweed: #344a21;
    --glutenfree: #f2b01c;
    --protein: #138c3e;
  }
  * { box-sizing: border-box; margin: 0; padding: 0; }
  html, body { width: 946px; height: 1200px; overflow: hidden; background: var(--page); }
  .range { position: relative; width: 946px; height: 1200px; }
  .label {
    position: absolute; width: 379px; height: 316px; background: var(--card);
    overflow: hidden; --accent: var(--herbs);
  }
  .label--herbs { left: 72px; top: 82px; --accent: var(--herbs); }
  .label--salt { left: 496px; top: 82px; --accent: var(--salt); }
  .label--spices { left: 72px; top: 442px; --accent: var(--spices); }
  .label--seaweed { left: 496px; top: 442px; --accent: var(--seaweed); }
  .label--glutenfree { left: 72px; top: 802px; --accent: var(--glutenfree); }
  .label--protein { left: 496px; top: 802px; --accent: var(--protein); }

  .title {
    position: absolute; left: 44px; top: 32px; width: 166px; font-family: "Amatic SC", cursive;
    font-weight: 700; line-height: 0.95; text-transform: uppercase; white-space: nowrap;
  }
  .title span { display: block; font-size: 62px; transform: scaleX(0.78); transform-origin: left center; }
  .title__organic { color: var(--accent); }
  .title__product { color: var(--ink); }

  .brand-leaf {
    position: absolute; left: 215px; top: 9px; width: 155px; height: 155px;
    background: var(--accent); border-radius: 78px 0 78px 0;
    display: flex; align-items: center; justify-content: center;
  }
  .brand-seal {
    width: 108px; height: 108px; border: 2px solid #fff; border-radius: 50%;
    display: flex; align-items: center; justify-content: center; text-align: center;
    font-family: "Oswald", sans-serif; font-weight: 500; color: #fff;
    font-size: 15px; line-height: 1.1; text-transform: uppercase; letter-spacing: 1px;
  }

  .variety-band {
    position: absolute; left: 18px; top: 174px; width: 246px; height: 56px;
    background: var(--accent); border-radius: 4px 26px 4px 26px;
  }
  .variety-name {
    position: absolute; left: 40px; top: 174px; font-family: "Amatic SC", cursive;
    font-weight: 700; font-size: 50px; color: #fff; line-height: 1; text-transform: uppercase;
    white-space: nowrap;
  }
  .variety-sub {
    position: absolute; font-family: "Amatic SC", cursive; font-weight: 700;
    font-size: 16px; line-height: 0.9; color: #b9e07a; text-transform: uppercase;
  }
  .illustration { position: absolute; border-radius: 50%; }

  .claims {
    position: absolute; left: 38px; top: 238px; display: grid;
    grid-template-columns: 62px 68px 84px;
    font-family: "Oswald", sans-serif; font-weight: 500; font-size: 15px;
    color: var(--claim-green); line-height: 18px; list-style: none;
  }
  .claims li { display: flex; align-items: center; gap: 3px; }
  .claims svg { width: 11px; height: 11px; flex: none; }
  .claims .no-icon { padding-left: 14px; }

  .origin {
    position: absolute; left: 40px; top: 281px; font-family: "Open Sans", sans-serif;
    font-size: 14px; color: var(--text);
  }
  .eu-badge {
    position: absolute; left: 280px; top: 179px; width: 53px; height: 35px; background: var(--eu-green);
  }
  .eu-caption {
    position: absolute; left: 256px; top: 214px; width: 100px; text-align: center;
    font-family: "Open Sans", sans-serif; font-size: 14px; line-height: 16px; color: var(--text);
  }
  .cert-badge {
    position: absolute; left: 270px; top: 253px; width: 34px; height: 30px;
    border-radius: 50%; background: var(--cert-red);
  }
  .cert-code {
    position: absolute; left: 256px; top: 287px; width: 100px; text-align: center;
    font-family: "Open Sans", sans-serif; font-size: 14px; color: var(--text);
  }
  .no-gluten-icon { position: absolute; left: 13px; top: 140px; width: 36px; height: 36px; }
</style>
</head>
<body>
<main class="range">

  <article class="label label--herbs">
    <h2 class="title"><span class="title__organic">Organic</span><span class="title__product">Crispbread</span></h2>
    <div class="brand-leaf"><div class="brand-seal">Havbo<br>Organic</div></div>
    <div class="variety-band"></div>
    <div class="illustration" role="img" aria-label="Rosemary sprigs and a basil leaf" style="left:150px;top:150px;width:86px;height:30px;background:linear-gradient(90deg,#7f9a5a,#4e7a34);"></div>
    <div class="variety-name">Herbs</div>
    <ul class="claims">
      <li><svg viewBox="0 0 10 10"><path d="M1 9C1 4 4 1 9 1 9 6 6 9 1 9Z" fill="currentColor"/></svg>Nature</li>
      <li><svg viewBox="0 0 10 10"><path d="M1 9C1 4 4 1 9 1 9 6 6 9 1 9Z" fill="currentColor"/></svg>Organic</li>
      <li><svg viewBox="0 0 10 10"><path d="M1 9C1 4 4 1 9 1 9 6 6 9 1 9Z" fill="currentColor"/></svg>Enviroment</li>
      <li><svg viewBox="0 0 10 10"><path d="M1 9C1 4 4 1 9 1 9 6 6 9 1 9Z" fill="currentColor"/></svg>Raw</li>
      <li><svg viewBox="0 0 10 10"><path d="M1 9C1 4 4 1 9 1 9 6 6 9 1 9Z" fill="currentColor"/></svg>Natural</li>
      <li class="no-icon">friendly</li>
    </ul>
    <p class="origin">Produced in: Denmark</p>
    <div class="eu-badge" role="img" aria-label="EU organic certification mark"></div>
    <p class="eu-caption">EU / ikke<br>EU-jordbrug</p>
    <div class="cert-badge" role="img" aria-label="State-controlled organic mark"></div>
    <p class="cert-code">QX-VAL-738</p>
  </article>

  <article class="label label--salt">
    <h2 class="title"><span class="title__organic">Organic</span><span class="title__product">Crispbread</span></h2>
    <div class="brand-leaf"><div class="brand-seal">Havbo<br>Organic</div></div>
    <div class="variety-band"></div>
    <div class="illustration" role="img" aria-label="Wooden bowl of sea salt with a spoon" style="left:130px;top:166px;width:56px;height:54px;background:radial-gradient(circle,#c9c2b4 30%,#4a3020 60%);"></div>
    <div class="variety-name">Salt</div>
    <ul class="claims">
      <li><svg viewBox="0 0 10 10"><path d="M1 9C1 4 4 1 9 1 9 6 6 9 1 9Z" fill="currentColor"/></svg>Nature</li>
      <li><svg viewBox="0 0 10 10"><path d="M1 9C1 4 4 1 9 1 9 6 6 9 1 9Z" fill="currentColor"/></svg>Organic</li>
      <li><svg viewBox="0 0 10 10"><path d="M1 9C1 4 4 1 9 1 9 6 6 9 1 9Z" fill="currentColor"/></svg>Enviroment</li>
      <li><svg viewBox="0 0 10 10"><path d="M1 9C1 4 4 1 9 1 9 6 6 9 1 9Z" fill="currentColor"/></svg>Raw</li>
      <li><svg viewBox="0 0 10 10"><path d="M1 9C1 4 4 1 9 1 9 6 6 9 1 9Z" fill="currentColor"/></svg>Natural</li>
      <li class="no-icon">friendly</li>
    </ul>
    <p class="origin">Produced in: Denmark</p>
    <div class="eu-badge" role="img" aria-label="EU organic certification mark"></div>
    <p class="eu-caption">EU / ikke<br>EU-jordbrug</p>
    <div class="cert-badge" role="img" aria-label="State-controlled organic mark"></div>
    <p class="cert-code">QX-VAL-738</p>
  </article>

  <article class="label label--spices">
    <h2 class="title"><span class="title__organic">Organic</span><span class="title__product">Crispbread</span></h2>
    <div class="brand-leaf"><div class="brand-seal">Havbo<br>Organic</div></div>
    <div class="variety-band"></div>
    <div class="illustration" role="img" aria-label="Star anise and a red chili pepper" style="left:146px;top:166px;width:110px;height:36px;background:linear-gradient(90deg,#3a1e12,#b3261a);"></div>
    <div class="variety-name">Spices</div>
    <ul class="claims">
      <li><svg viewBox="0 0 10 10"><path d="M1 9C1 4 4 1 9 1 9 6 6 9 1 9Z" fill="currentColor"/></svg>Nature</li>
      <li><svg viewBox="0 0 10 10"><path d="M1 9C1 4 4 1 9 1 9 6 6 9 1 9Z" fill="currentColor"/></svg>Organic</li>
      <li><svg viewBox="0 0 10 10"><path d="M1 9C1 4 4 1 9 1 9 6 6 9 1 9Z" fill="currentColor"/></svg>Enviroment</li>
      <li><svg viewBox="0 0 10 10"><path d="M1 9C1 4 4 1 9 1 9 6 6 9 1 9Z" fill="currentColor"/></svg>Raw</li>
      <li><svg viewBox="0 0 10 10"><path d="M1 9C1 4 4 1 9 1 9 6 6 9 1 9Z" fill="currentColor"/></svg>Natural</li>
      <li class="no-icon">friendly</li>
    </ul>
    <p class="origin">Produced in: Denmark</p>
    <div class="eu-badge" role="img" aria-label="EU organic certification mark"></div>
    <p class="eu-caption">EU / ikke<br>EU-jordbrug</p>
    <div class="cert-badge" role="img" aria-label="State-controlled organic mark"></div>
    <p class="cert-code">QX-VAL-738</p>
  </article>

  <article class="label label--seaweed">
    <h2 class="title"><span class="title__organic">Organic</span><span class="title__product">Crispbread</span></h2>
    <div class="brand-leaf"><div class="brand-seal">Havbo<br>Organic</div></div>
    <div class="variety-band"></div>
    <div class="illustration" role="img" aria-label="Green seaweed sprig" style="left:172px;top:158px;width:56px;height:66px;background:linear-gradient(180deg,#8fbf4a,#4d7a2a);"></div>
    <div class="variety-name">Seaweed</div>
    <ul class="claims">
      <li><svg viewBox="0 0 10 10"><path d="M1 9C1 4 4 1 9 1 9 6 6 9 1 9Z" fill="currentColor"/></svg>Nature</li>
      <li><svg viewBox="0 0 10 10"><path d="M1 9C1 4 4 1 9 1 9 6 6 9 1 9Z" fill="currentColor"/></svg>Organic</li>
      <li><svg viewBox="0 0 10 10"><path d="M1 9C1 4 4 1 9 1 9 6 6 9 1 9Z" fill="currentColor"/></svg>Enviroment</li>
      <li><svg viewBox="0 0 10 10"><path d="M1 9C1 4 4 1 9 1 9 6 6 9 1 9Z" fill="currentColor"/></svg>Raw</li>
      <li><svg viewBox="0 0 10 10"><path d="M1 9C1 4 4 1 9 1 9 6 6 9 1 9Z" fill="currentColor"/></svg>Natural</li>
      <li class="no-icon">friendly</li>
    </ul>
    <p class="origin">Produced in: Denmark</p>
    <div class="eu-badge" role="img" aria-label="EU organic certification mark"></div>
    <p class="eu-caption">EU / ikke<br>EU-jordbrug</p>
    <div class="cert-badge" role="img" aria-label="State-controlled organic mark"></div>
    <p class="cert-code">QX-VAL-738</p>
  </article>

  <article class="label label--glutenfree">
    <h2 class="title"><span class="title__organic">Organic</span><span class="title__product">Crispbread</span></h2>
    <div class="brand-leaf"><div class="brand-seal">Havbo<br>Organic</div></div>
    <div class="variety-band"></div>
    <svg class="no-gluten-icon" viewBox="0 0 40 40" role="img" aria-label="Gluten free">
      <circle cx="20" cy="20" r="17" fill="#fff" stroke="#e2231a" stroke-width="4"/>
      <line x1="8" y1="8" x2="32" y2="32" stroke="#e2231a" stroke-width="4"/>
    </svg>
    <div class="variety-name">Glutenfree</div>
    <ul class="claims">
      <li><svg viewBox="0 0 10 10"><path d="M1 9C1 4 4 1 9 1 9 6 6 9 1 9Z" fill="currentColor"/></svg>Nature</li>
      <li><svg viewBox="0 0 10 10"><path d="M1 9C1 4 4 1 9 1 9 6 6 9 1 9Z" fill="currentColor"/></svg>Organic</li>
      <li><svg viewBox="0 0 10 10"><path d="M1 9C1 4 4 1 9 1 9 6 6 9 1 9Z" fill="currentColor"/></svg>Enviroment</li>
      <li><svg viewBox="0 0 10 10"><path d="M1 9C1 4 4 1 9 1 9 6 6 9 1 9Z" fill="currentColor"/></svg>Raw</li>
      <li><svg viewBox="0 0 10 10"><path d="M1 9C1 4 4 1 9 1 9 6 6 9 1 9Z" fill="currentColor"/></svg>Natural</li>
      <li class="no-icon">friendly</li>
    </ul>
    <p class="origin">Produced in: Denmark</p>
    <div class="eu-badge" role="img" aria-label="EU organic certification mark"></div>
    <p class="eu-caption">EU / ikke<br>EU-jordbrug</p>
    <div class="cert-badge" role="img" aria-label="State-controlled organic mark"></div>
    <p class="cert-code">QX-VAL-738</p>
  </article>

  <article class="label label--protein">
    <h2 class="title"><span class="title__organic">Organic</span><span class="title__product">Crispbread</span></h2>
    <div class="brand-leaf"><div class="brand-seal">Havbo<br>Organic</div></div>
    <div class="variety-band"></div>
    <div class="illustration" role="img" aria-label="Sage leaf" style="left:16px;top:130px;width:30px;height:60px;border-radius:50% 50% 50% 50% / 60% 60% 40% 40%;background:linear-gradient(180deg,#9aae7c,#6d8a52);"></div>
    <div class="variety-name">Protein</div>
    <div class="variety-sub" style="left:186px;top:188px;">Green<br>Proteins</div>
    <ul class="claims">
      <li><svg viewBox="0 0 10 10"><path d="M1 9C1 4 4 1 9 1 9 6 6 9 1 9Z" fill="currentColor"/></svg>Nature</li>
      <li><svg viewBox="0 0 10 10"><path d="M1 9C1 4 4 1 9 1 9 6 6 9 1 9Z" fill="currentColor"/></svg>Organic</li>
      <li><svg viewBox="0 0 10 10"><path d="M1 9C1 4 4 1 9 1 9 6 6 9 1 9Z" fill="currentColor"/></svg>Enviroment</li>
      <li><svg viewBox="0 0 10 10"><path d="M1 9C1 4 4 1 9 1 9 6 6 9 1 9Z" fill="currentColor"/></svg>Raw</li>
      <li><svg viewBox="0 0 10 10"><path d="M1 9C1 4 4 1 9 1 9 6 6 9 1 9Z" fill="currentColor"/></svg>Natural</li>
      <li class="no-icon">friendly</li>
    </ul>
    <p class="origin">Produced in: Denmark</p>
    <div class="eu-badge" role="img" aria-label="EU organic certification mark"></div>
    <p class="eu-caption">EU / ikke<br>EU-jordbrug</p>
    <div class="cert-badge" role="img" aria-label="State-controlled organic mark"></div>
    <p class="cert-code">QX-VAL-738</p>
  </article>

</main>
</body>
</html>
```